regPersonal Trainer Flyer Design

Reason: I have been very busy with other work and would like to extend the deadline to offer designers the chance to edit and improve designs with my help. Thank you for all the designs that have been sent so far.

```html
<!DOCTYPE html>
<html lang="en">
<head>
<meta charset="utf-8">
<title>Fitness Training – Personal Trainer Flyer</title>
<link rel="stylesheet" href="https://fonts.googleapis.com/css2?family=PT+Sans:wght@400;700&family=Open+Sans:wght@700;800&display=swap">
<style>
  :root {
    --blue: #0b5fb5;
    --blue-light: #5d8fd2;
    --black: #000000;
    --white: #ffffff;
    --yellow: #f3c12f;
    --ring: #c3cbea;
    --burst-edge: #9a9aa6;
    --photo-warm: #d9b9a4;
    --photo-cool: #8c8f9e;
  }
  * { margin: 0; padding: 0; box-sizing: border-box; }
  html, body { width: 1200px; height: 851px; overflow: hidden; background: var(--blue); }
  .flyer {
    position: relative;
    width: 1200px;
    height: 851px;
    overflow: hidden;
    background: var(--blue);
    font-family: "PT Sans", Arial, sans-serif;
    color: var(--white);
  }
  .shapes { position: absolute; inset: 0; }

  .headline { position: absolute; left: 104px; top: 62px; }
  .headline__main {
    display: block;
    font-family: "Open Sans", Arial, sans-serif;
    font-weight: 800;
    font-size: 140px;
    line-height: 1;
    letter-spacing: -4px;
  }
  .headline__sub {
    display: block;
    margin-top: 12px;
    font-family: "Open Sans", Arial, sans-serif;
    font-weight: 700;
    font-size: 66px;
    line-height: 1;
    letter-spacing: 17px;
  }
  .headline__tag {
    display: block;
    margin-top: 8px;
    font-size: 52px;
    line-height: 1;
    color: var(--yellow);
  }

  .benefits {
    position: absolute;
    left: 116px;
    top: 356px;
    list-style: none;
    font-weight: 700;
    font-size: 27px;
    line-height: 36px;
  }
  .benefits li { position: relative; padding-left: 32px; }
  .benefits li::before {
    content: "";
    position: absolute;
    left: 0;
    top: 10px;
    border-left: 12px solid var(--yellow);
    border-top: 8px solid transparent;
    border-bottom: 8px solid transparent;
  }

  .offer {
    position: absolute;
    left: 552px;
    top: 326px;
    width: 212px;
    text-align: center;
    color: var(--black);
    font-weight: 700;
    line-height: 1;
  }
  .offer__one, .offer__session { display: block; font-size: 42px; }
  .offer__free { display: block; font-size: 60px; margin: 2px 0; }

  .trainer { position: absolute; left: 124px; top: 664px; }
  .trainer__name { font-size: 50px; font-weight: 700; line-height: 1; }
  .trainer__role {
    margin-top: 30px;
    font-size: 29px;
    line-height: 1;
    letter-spacing: 2px;
    color: var(--yellow);
  }

  .contact {
    position: absolute;
    left: 726px;
    top: 690px;
    list-style: none;
    font-weight: 700;
    font-size: 26px;
  }
  .contact li { display: flex; align-items: center; height: 36px; margin-bottom: 14px; }
  .contact svg { width: 36px; height: 36px; margin-right: 20px; flex: none; }
</style>
</head>
<body>
<div class="flyer">
  <svg class="shapes" width="1200" height="851" viewBox="0 0 1200 851">
    <defs>
      <polygon id="hex" points="106,0 53,91.8 -53,91.8 -106,0 -53,-91.8 53,-91.8"/>
      <linearGradient id="photo-tone" x1="0" y1="0" x2="1" y2="1">
        <stop offset="0" stop-color="var(--photo-warm)"/>
        <stop offset="1" stop-color="var(--photo-cool)"/>
      </linearGradient>
      <linearGradient id="portrait-tone" x1="0" y1="0" x2="0" y2="1">
        <stop offset="0" stop-color="#c9a58e"/>
        <stop offset="0.6" stop-color="#7b6a64"/>
        <stop offset="1" stop-color="#1b2c48" stop-opacity="0"/>
      </linearGradient>
    </defs>

    <rect class="band-black" x="0" y="322" width="1200" height="314" fill="var(--black)"/>
    <rect class="band-light" x="0" y="636" width="1200" height="32" fill="var(--blue-light)"/>
    <rect class="band-name" x="0" y="636" width="500" height="92" fill="var(--blue-light)"/>

    <g class="photo photo--main" role="img" aria-label="Photo of a trainer coaching a client through a squat in a studio">
      <circle cx="948" cy="240" r="198" fill="var(--ring)"/>
      <circle cx="948" cy="240" r="184" fill="url(#photo-tone)"/>
    </g>
    <g class="photo photo--small" role="img" aria-label="Photo of a client working on a boxing pad">
      <circle cx="898" cy="528" r="114" fill="var(--ring)"/>
      <circle cx="898" cy="528" r="101" fill="url(#photo-tone)"/>
    </g>

    <g class="burst" transform="translate(658 406)">
      <g stroke="var(--burst-edge)" stroke-width="6" fill="var(--burst-edge)">
        <use href="#hex"/>
        <use href="#hex" transform="rotate(12)"/>
        <use href="#hex" transform="rotate(24)"/>
        <use href="#hex" transform="rotate(36)"/>
        <use href="#hex" transform="rotate(48)"/>
      </g>
      <g fill="var(--yellow)">
        <use href="#hex"/>
        <use href="#hex" transform="rotate(12)"/>
        <use href="#hex" transform="rotate(24)"/>
        <use href="#hex" transform="rotate(36)"/>
        <use href="#hex" transform="rotate(48)"/>
      </g>
    </g>

    <g class="portrait" role="img" aria-label="Head-and-shoulders photo of the personal trainer">
      <rect x="450" y="558" width="216" height="293" rx="60" fill="url(#portrait-tone)"/>
    </g>
  </svg>

  <h1 class="headline">
    <span class="headline__main">FITNESS</span>
    <span class="headline__sub">TRAINING</span>
    <span class="headline__tag">can be at your home</span>
  </h1>

  <ul class="benefits">
    <li>Lacking motivation?</li>
    <li>Not achieving your goals?</li>
    <li>Need help?</li>
    <li>Bored of the gym?</li>
    <li>You're never too old</li>
    <li>I can help improve your<br>health and well-being</li>
  </ul>

  <p class="offer">
    <span class="offer__one">One</span>
    <span class="offer__free">FREE</span>
    <span class="offer__session">Session</span>
  </p>

  <div class="trainer">
    <p class="trainer__name">Sam Carden</p>
    <p class="trainer__role">Personal Trainer</p>
  </div>

  <ul class="contact">
    <li>
      <svg viewBox="0 0 36 36" aria-hidden="true">
        <circle cx="18" cy="18" r="18" fill="var(--yellow)"/>
        <path d="M13 9 h4 l1 5 -2.5 2 a10 10 0 0 0 5 5 l2 -2.5 5 1 v4 a2 2 0 0 1 -2 2 A16 16 0 0 1 11 11 a2 2 0 0 1 2 -2z" fill="var(--blue)"/>
      </svg>
      07700900418
    </li>
    <li>
      <svg viewBox="0 0 36 36" aria-hidden="true">
        <circle cx="18" cy="18" r="18" fill="var(--yellow)"/>
        <rect x="8" y="11" width="20" height="14" fill="var(--white)"/>
        <path d="M8 11 L18 19 L28 11" fill="none" stroke="var(--yellow)" stroke-width="1.8"/>
      </svg>
      samcarden@fitmail.co.uk
    </li>
  </ul>
</div>
</body>
</html>
```